A5 flyer recto (just the front side) announcing the summer events

For a public aquarium in France, we invite you to create our A5 flyer recto (just the front side) announcing the events of this summer 2015
The flyer must be written in french, you will find attached all the text that you have to fill in the flyer.
You also have to use our logo in the top or in the bottom of the flyer (2 versions of the logo four color or black and white version. According your design you can use one of them)
We also have a mascot ( a sea horse), you can use it if you want to illustrate your design (attachment file)
We manage a mini-golf and we want to promote it with a special discount, you have to mentioned this benefit in the flyer as a special discount coupon)
You must specify our website and our adress..
We remain at your disposal for any question

```html
<!DOCTYPE html>
<html lang="fr">
<head>
<meta charset="utf-8">
<title>Aquarium de Kerlann – Été 2015</title>
<link href="https://fonts.googleapis.com/css2?family=Quicksand:wght@400;500;700&display=swap" rel="stylesheet">
<style>
  :root{
    --peach:#f3c9a4;
    --sand:#eab27a;
    --orange:#e3a24a;
    --crimson:#cf1346;
    --coupon-red:#d81f26;
    --coupon-dark:#7a0b10;
    --lime:#d9e04e;
    --text-light:#fff7ee;
    --brand-blue:#27406e;
  }
  *{margin:0;padding:0;box-sizing:border-box}
  html,body{width:846px;height:1200px;overflow:hidden}
  body{font-family:"Quicksand",sans-serif;background:var(--sand)}
  .flyer{
    position:relative;width:846px;height:1200px;overflow:hidden;
    background:linear-gradient(180deg,#f7dcc6 0%,var(--peach) 30%,var(--sand) 60%,var(--orange) 100%);
  }
  .hero-photo{
    position:absolute;left:120px;top:0;width:726px;height:370px;
    background:radial-gradient(ellipse at 60% 40%,#fff3d6 0%,#f8d27a 35%,#f2a6a0 70%,rgba(243,201,164,0) 100%);
  }
  .swoosh{position:absolute;left:0;top:0}
  .brand{
    position:absolute;left:40px;top:250px;
    font-weight:700;font-size:54px;line-height:1;color:var(--brand-blue);
    display:flex;align-items:center;gap:14px;
  }
  .brand-dot{width:22px;height:22px;border-radius:50%;background:var(--brand-blue)}
  .programme{
    position:absolute;left:115px;top:428px;width:680px;
    color:var(--text-light);font-size:18px;line-height:23.5px;font-weight:500;
  }
  .programme .headline{color:var(--crimson);font-weight:700;font-size:16.5px}
  .programme .date{color:var(--crimson);font-size:21px}
  .programme .highlight{color:var(--lime);font-weight:700}
  .mascot{
    position:absolute;left:0;top:740px;width:170px;height:430px;
    background:radial-gradient(ellipse at 50% 45%,#b8dc4a 0%,#8fc23a 45%,rgba(143,194,58,0) 75%);
    z-index:3;
  }
  .coupon{
    position:absolute;left:90px;top:862px;width:756px;height:130px;
    background:linear-gradient(90deg,var(--coupon-dark) 0%,#b5141b 35%,var(--coupon-red) 100%);
  }
  .coupon-flap{
    position:absolute;left:0;top:898px;width:175px;height:125px;
    background:linear-gradient(90deg,var(--coupon-red),var(--coupon-dark));
  }
  .coupon-offer{
    position:absolute;left:140px;top:902px;width:620px;text-align:center;
    color:#fff;font-weight:700;font-size:18.5px;line-height:24px;
  }
  .coupon-note{
    position:absolute;left:260px;top:992px;color:#fff;font-size:14px;font-weight:500;
  }
  .contact{
    position:absolute;left:90px;top:1067px;width:756px;text-align:center;color:#fff;
    font-weight:700;font-size:15.5px;line-height:22px;
  }
  .contact .address{margin-top:10px}
  .contact .phone{font-size:33px;margin-top:20px;line-height:1}
</style>
</head>
<body>
<div class="flyer">
  <div class="hero-photo" role="img" aria-label="Photo de deux jeunes filles joyeuses levant le pouce devant des ballons colorés"></div>

  <svg class="swoosh" width="846" height="460" viewBox="0 0 846 460" aria-hidden="true">
    <path d="M0 255 C200 250 330 320 470 330 C620 340 760 220 846 75 L846 115 C770 270 620 385 470 380 C330 375 220 300 0 290 Z" fill="#cf1346"/>
    <path d="M0 290 C220 300 330 375 470 380 C600 385 720 320 800 240 C720 340 600 400 470 400 C330 400 220 330 0 320 Z" fill="#f4d2b6" opacity="0.8"/>
  </svg>

  <div class="brand"><span class="brand-dot"></span>Aquarium de Kerlann</div>

  <div class="programme">
    <p class="headline">TOUS LES JOURS, ANIMATIONS « BASSIN TACTILE » COMMENTÉES.</p>
    <p>Tous les après-midis Nourrissages commentés de nos espèces aquatiques.</p>
    <p><span class="date">Les mardis 21 &amp; 28 juillet, 4 &amp; 11 août de 20h à 23h</span>, les <span class="highlight">NOCTURNES DE L'AQUARIUM</span>, avis de tempête.</p>
    <p>Découvrez l'aquarium de Kerlann comme vous ne l'avez jamais visité. 4 comédiens investissent l'aquarium pour une visite drôle et décalée à faire en famille.</p>
    <p><span class="date">Les jeudis 9 &amp; 16 juillet, 20 &amp; 27 août de 14h à 17h</span> pour les enfants de 6 à 12 ans, l'aquarium propose des ateliers scientifiques. En compagnie d'un animateur, l'occasion d'apprendre en s'amusant.</p>
    <p><span class="date">En juillet &amp; août,</span> Exposition « Laisse de Mer, source de vie » de Claire Morvan.</p>
    <p>Mieux comprendre la laisse de mer, son rôle écologique, son utilité pour nos plages…</p>
  </div>

  <div class="coupon-flap"></div>
  <div class="coupon"></div>
  <p class="coupon-offer">Sur présentation de ce coupon, bénéficiez d'une partie mini-golf enfant offerte pour une partie mini-golf adulte achetée *</p>
  <p class="coupon-note">*offre non cumulable avec toute autre promotion</p>

  <div class="mascot" role="img" aria-label="Illustration de la mascotte, un hippocampe vert"></div>

  <div class="contact">
    <p>Retrouvez toutes les informations, tarif, horaires et conditions d'inscriptions sur :<br>aquariumdekerlann.fr</p>
    <p class="address">Aquarium de Kerlann&nbsp; 14, rue des Goélands 56000 VANNES</p>
    <p class="phone">02 00 48 26 15</p>
  </div>
</div>
</body>
</html>
```